Tour Company Needs Poster for Box Office

We need a poster to promote walking tours in Aspen, Colorado. It should be attention grabbing with a vintage look similar to old west shows or circus promotions. It needs to promote "Ridgeline Stroll Tours" 3 different tours (an evening ghost tour "Birchvale's NightVeil", a classic historic tour "Birchvale's Then and Now" & a sightseeing tour "Beyond the Quiet Lane"). Attached images should be used in conjunction with the different tour promotions. Poster should be full color and the size needs to be 24" wide X 36 " high.

Requirements
Must have
• Individual tour tag lines
Birchvale's NightVeil "Ghosts Murder & Mayhem"
Birchvale's Then and Now" Classic Historical Tour"
Beyond the Quiet Lane "Historic West End to the River"

Company Logo can be small towards the bottom of the poster and paired with the quote "Like Marlow he Loves Spinning Tales! -Kellaway's Journeys"

website should be included www.RidgelineStrollTours.example
Nice to have
• Small Quotes to include
"theatrics, humor, wit and dazzling manner"
"awesome story teller"
"should not be missed"

```html
<!DOCTYPE html>
<html lang="en">
<head>
<meta charset="utf-8">
<title>Ridgeline Stroll Tours – Poster</title>
<link rel="stylesheet" href="https://fonts.googleapis.com/css2?family=Anton&family=Oswald:wght@500;600&display=swap">
<style>
  :root {
    --cream: #f6e9d9;
    --salmon: #ef7f6b;
    --ink: #111111;
    --photo-dark: #6f6a66;
    --photo-light: #b9b2ab;
    --post-tone: #8c8f92;
  }
  * { margin: 0; padding: 0; box-sizing: border-box; }
  html, body { width: 800px; height: 1200px; overflow: hidden; background: var(--cream); }
  .poster {
    position: relative; width: 800px; height: 1200px;
    background: var(--cream); color: var(--ink);
    font-family: "Anton", "Impact", sans-serif;
    overflow: hidden;
  }
  .abs { position: absolute; white-space: nowrap; line-height: 1; }

  .masthead {
    position: absolute; left: 68px; top: 17px; width: 697px; height: 113px;
    background: var(--ink); display: flex; align-items: center; justify-content: center;
  }
  .masthead__name { color: var(--salmon); font-size: 68px; letter-spacing: 2px; }

  .dateline { top: 162px; font-size: 30px; }
  .dateline--left { left: 32px; }
  .dateline--right { right: 32px; }

  .tour {
    position: absolute; left: 32px; width: 736px; height: 196px;
    background: var(--salmon);
  }
  .tour--night { top: 215px; }
  .tour--history { top: 420px; }
  .tour--lane { top: 626px; }
  .tour__type { position: absolute; left: 0; top: 0; width: 736px; height: 196px; overflow: visible; }
  .tour__type text { fill: var(--ink); font-family: "Anton", "Impact", sans-serif; }
  .tour__type .schedule { font-family: "Oswald", sans-serif; font-weight: 600; }
  .photo {
    position: absolute;
    background: linear-gradient(180deg, var(--photo-light), var(--photo-dark));
  }
  .signpost {
    position: absolute;
    background: linear-gradient(180deg, var(--post-tone), #55595d);
  }

  .quote-band { position: absolute; background: var(--salmon); }
  .quote-box {
    position: absolute; background: var(--cream); border: 3px solid var(--ink);
    display: flex; align-items: center; justify-content: center;
    font-family: "Oswald", sans-serif; font-weight: 600; color: var(--ink);
  }
  .deco-star { position: absolute; width: 56px; height: 56px; }

  .ticket-box {
    position: absolute; left: 116px; top: 1084px; width: 565px; height: 90px;
    background: var(--salmon); border: 5px solid var(--ink);
    display: flex; flex-direction: column; align-items: center; justify-content: center; gap: 8px;
  }
  .ticket-box__lead { font-family: "Oswald", sans-serif; font-weight: 600; font-size: 15px; }
  .ticket-box__url { font-family: "Oswald", sans-serif; font-weight: 600; font-size: 24px; }

  .brand-block {
    position: absolute; left: 692px; top: 1112px; width: 100px;
    font-family: "Oswald", sans-serif; font-weight: 600; color: var(--ink);
  }
  .brand-block__quote { font-size: 8px; line-height: 1.2; margin-bottom: 4px; }
  .brand-block__mark { display: flex; align-items: center; gap: 4px; font-size: 10px; line-height: 1.1; }
  .brand-block__dot { width: 10px; height: 10px; background: var(--salmon); flex: none; }
</style>
</head>
<body>
<main class="poster">
  <header class="masthead">
    <span class="masthead__name">RIDGELINE STROLL TOURS</span>
  </header>

  <p class="abs dateline dateline--left">Aspen, Colorado</p>
  <p class="abs dateline dateline--right">Presents...</p>

  <section class="tour tour--night">
    <div class="photo" style="left:14px;top:2px;width:157px;height:192px;" role="img" aria-label="Photo of two costumed guides in Victorian dress holding a lantern"></div>
    <svg class="tour__type" viewBox="0 0 736 196">
      <text x="145" y="69" font-size="62" textLength="580" lengthAdjust="spacingAndGlyphs">BIRCHVALE'S NIGHTVEIL</text>
      <text x="183" y="130" font-size="66" textLength="292" lengthAdjust="spacingAndGlyphs">Ghosts, Murderers</text>
      <text class="schedule" x="482" y="90" font-size="19" textLength="30" lengthAdjust="spacingAndGlyphs">9pm</text>
      <path transform="translate(516 72) scale(0.85)" d="M12 1l3.3 7.2 7.7.8-5.8 5.2 1.7 7.6L12 17.9 5.1 21.8l1.7-7.6L1 9l7.7-.8z" fill="#111"/>
      <text class="schedule" x="540" y="90" font-size="19" textLength="188" lengthAdjust="spacingAndGlyphs">Tuesday and Friday.</text>
      <text x="446" y="176" font-size="15" textLength="30" lengthAdjust="spacingAndGlyphs">AND</text>
      <text x="485" y="176" font-size="64" textLength="241" lengthAdjust="spacingAndGlyphs">Mayhem</text>
    </svg>
  </section>

  <section class="tour tour--history">
    <svg class="tour__type" viewBox="0 0 736 196">
      <text x="9" y="51" font-size="50" textLength="579" lengthAdjust="spacingAndGlyphs">BIRCHVALE'S THEN AND NOW</text>
      <text x="9" y="148" font-size="104" textLength="331" lengthAdjust="spacingAndGlyphs">Classical</text>
      <text class="schedule" x="384" y="80" font-size="17" textLength="40" lengthAdjust="spacingAndGlyphs">11am</text>
      <path transform="translate(428 63) scale(0.8)" d="M12 1l3.3 7.2 7.7.8-5.8 5.2 1.7 7.6L12 17.9 5.1 21.8l1.7-7.6L1 9l7.7-.8z" fill="#111"/>
      <text class="schedule" x="452" y="80" font-size="17" textLength="139" lengthAdjust="spacingAndGlyphs">Monday, Wednesday</text>
      <text class="schedule" x="461" y="113" font-size="17" textLength="70" lengthAdjust="spacingAndGlyphs">and Thursday</text>
      <text x="156" y="186" font-size="32" textLength="186" lengthAdjust="spacingAndGlyphs">Historical</text>
      <text x="348" y="189" font-size="78" textLength="134" lengthAdjust="spacingAndGlyphs">Tour</text>
    </svg>
    <div class="photo" style="left:613px;top:7px;width:109px;height:185px;" role="img" aria-label="Photo of a guide in a cowboy hat and vest"></div>
  </section>

  <section class="tour tour--lane">
    <div class="signpost" style="left:33px;top:12px;width:109px;height:180px;" role="img" aria-label="Illustration of a wooden signpost with tour direction signs"></div>
    <svg class="tour__type" viewBox="0 0 736 196">
      <text x="145" y="64" font-size="62" textLength="588" lengthAdjust="spacingAndGlyphs">BEYOND THE QUIET LANE</text>
      <text x="211" y="149" font-size="98" textLength="242" lengthAdjust="spacingAndGlyphs">Historic</text>
      <text x="461" y="106" font-size="34" textLength="87" lengthAdjust="spacingAndGlyphs">to the</text>
      <text x="313" y="186" font-size="34" textLength="140" lengthAdjust="spacingAndGlyphs">West End</text>
      <text x="461" y="188" font-size="92" textLength="166" lengthAdjust="spacingAndGlyphs">River</text>
    </svg>
  </section>

  <svg class="deco-star" style="left:12px;top:872px;" viewBox="0 0 24 24"><path d="M12 1l3.3 7.2 7.7.8-5.8 5.2 1.7 7.6L12 17.9 5.1 21.8l1.7-7.6L1 9l7.7-.8z" fill="#111"/></svg>
  <svg class="deco-star" style="left:730px;top:872px;" viewBox="0 0 24 24"><path d="M12 1l3.3 7.2 7.7.8-5.8 5.2 1.7 7.6L12 17.9 5.1 21.8l1.7-7.6L1 9l7.7-.8z" fill="#111"/></svg>
  <div class="quote-band" style="left:72px;top:849px;width:656px;height:102px;border-radius:30px;"></div>
  <div class="quote-box" style="left:92px;top:862px;width:636px;height:77px;font-size:36px;">“Theatrics, humor, wit and dazzling manner”</div>

  <svg style="position:absolute;left:25px;top:956px;" width="738" height="116" viewBox="0 0 738 116">
    <path d="M60 0 H708 Q738 0 738 30 V86 Q738 116 708 116 H60 L0 58 Z" fill="#ef7f6b"/>
  </svg>
  <div class="quote-box" style="left:61px;top:974px;width:323px;height:81px;font-size:30px;">“Should not be missed”</div>
  <div class="quote-box" style="left:402px;top:974px;width:323px;height:81px;font-size:30px;">“Awesome story teller”</div>

  <footer class="ticket-box">
    <p class="ticket-box__lead">For more information and to purchase tickets go to</p>
    <p class="ticket-box__url">www.RidgelineStrollTours.example</p>
  </footer>

  <div class="brand-block">
    <p class="brand-block__quote">“Like Marlow he Loves Spinning Tales!” –Kellaway's Journeys</p>
    <div class="brand-block__mark">
      <span class="brand-block__dot"></span>
      <span>Ridgeline Stroll Tours</span>
    </div>
  </div>
</main>
</body>
</html>
```